K7 Electrical Services Ltd Web design

I require a web site for my new electrical contracting company. We are customer service orientated. Offering high value electrical installations, design and maintenance. Focused on custom residential and commercial upgrading. Lighting design and application are paramount in our company's services. Industry leading product use and integration are always on the forefront with our customer client services. As well as energy efficiency.

Target Market(s)

Homebuilders, General Contractors, Property management companies, clients, individuals,

Industry/Entity Type

Electric Company

Coding

Coded - Design and coding required

Number of Pages Required

3 page

Requirements
Must have
• Classic, modern, edgy but not trendy . Appeals to the masse.
• 3 page
• home page
• about page
• gallery page
• ability to contact from the webiste
Nice to have
• open to all types of designs that are relative to the construction industry.
• Black, Grey, metallic ice blue and deep purple colours from the logo.
Should not have
• anything cheesy with cartoon light bulb images.

```html
<!DOCTYPE html>
<html lang="en">
<head>
<meta charset="utf-8">
<title>K7 Electrical Services Ltd</title>
<link href="https://fonts.googleapis.com/css2?family=Open+Sans:wght@400;600;700&family=Raleway:wght@400;500;700;800&display=swap" rel="stylesheet">
<style>
:root{
  --purple:#5b2d8e;
  --purple-deep:#4a2275;
  --purple-dark:#3a1a5e;
  --ink:#2b2b2b;
  --grey:#6d6d6d;
  --light:#f4f4f6;
  --white:#ffffff;
}
*{margin:0;padding:0;box-sizing:border-box}
html,body{width:1200px;height:2464px;overflow:hidden;background:var(--white)}
body{font-family:"Open Sans",Arial,sans-serif;color:var(--ink)}
.site-header{height:120px;display:flex;align-items:center;justify-content:space-between;padding:0 116px 0 52px}
.brand{display:flex;align-items:center;gap:10px;color:var(--purple);font-family:"Raleway",Arial,sans-serif;font-weight:700;font-size:20px;line-height:1;white-space:nowrap}
.brand-mark{width:16px;height:16px;background:currentColor;flex:none}
.main-nav{display:flex;gap:44px;font-family:"Raleway",Arial,sans-serif;font-size:14px;font-weight:500;text-transform:uppercase}
.main-nav a{color:var(--grey);text-decoration:none;padding-bottom:8px}
.main-nav a.active{color:var(--purple);border-bottom:2px solid var(--purple)}
.hero{position:relative;height:640px;overflow:hidden}
.hero-photo{position:absolute;inset:0;background:linear-gradient(180deg,#8a8fb8 0%,#5a5c88 35%,#3f3a5a 55%,#7a5a3a 75%,#3d4a2e 100%)}
.hero-content{position:relative;text-align:center;color:var(--white);padding-top:165px}
.hero-title{font-family:"Raleway",Arial,sans-serif;font-weight:800;font-size:118px;letter-spacing:3px;line-height:1}
.hero-tagline{font-size:24px;margin-top:18px}
.hero-wave{position:absolute;left:0;bottom:-1px;width:1200px;height:130px}
.section-heading{display:flex;align-items:center;justify-content:center;gap:22px;font-family:"Raleway",Arial,sans-serif;font-size:38px;font-weight:500;color:var(--ink)}
.section-heading::before,.section-heading::after{content:"";width:110px;height:2px;background:var(--purple)}
.welcome{padding:38px 150px 0;height:360px}
.welcome p{font-size:14px;line-height:24px;color:var(--grey);text-align:center;margin-top:26px}
.about{position:relative;height:420px;overflow:hidden}
.about-photo{position:absolute;inset:0;background:linear-gradient(180deg,#7a6b8e 0%,#5d4f73 50%,#3e3452 100%)}
.about-content{position:relative;text-align:center;color:var(--white);padding:70px 220px 0}
.about .section-heading{color:var(--white)}
.about .section-heading::before,.about .section-heading::after{background:var(--white)}
.about p{font-size:15px;line-height:25px;margin-top:22px}
.btn-outline{display:inline-block;margin-top:30px;border:2px solid var(--white);color:var(--white);font-family:"Raleway",Arial,sans-serif;font-weight:700;font-size:16px;letter-spacing:1px;padding:12px 30px;text-decoration:none}
.services{padding:116px 100px 0;height:672px}
.service-list{display:flex;justify-content:space-between;margin-top:50px}
.service{width:300px;text-align:center}
.service-icon{width:164px;height:164px;border-radius:50%;background:var(--purple);margin:0 auto;display:flex;align-items:center;justify-content:center;border:6px solid #e8e1f0}
.service h3{font-family:"Raleway",Arial,sans-serif;font-weight:500;font-size:24px;margin-top:36px}
.service p{font-size:13px;line-height:20px;color:var(--grey);margin-top:12px;height:40px}
.btn-small{display:inline-flex;align-items:center;gap:6px;margin-top:24px;border:2px solid var(--ink);color:var(--ink);font-size:12px;font-weight:700;padding:7px 14px;text-decoration:none}
.site-footer{background:var(--purple);height:188px;color:var(--white);display:flex;padding:42px 100px 0 110px}
.footer-about{width:360px}
.footer-about .brand{color:var(--white);font-size:18px}
.footer-about .brand-mark{width:14px;height:14px}
.footer-about p{font-size:11px;line-height:17px;margin-top:16px;opacity:.9;width:300px}
.footer-contact{width:300px}
.footer-title{font-family:"Raleway",Arial,sans-serif;font-size:18px;font-weight:500;text-transform:uppercase;margin-bottom:14px}
.footer-contact ul{list-style:none;font-size:12px;line-height:27px}
.footer-contact li{display:flex;align-items:center;gap:10px}
.footer-news p{font-size:12px;margin-bottom:10px}
.subscribe{display:flex}
.subscribe span{width:180px;height:34px;background:var(--white)}
.subscribe b{background:var(--purple-dark);font-size:12px;font-weight:600;padding:0 16px;display:flex;align-items:center}
.socials{display:flex;gap:10px;margin-top:14px}
.socials i{width:30px;height:30px;border-radius:50%;background:var(--white);opacity:.85}
.footer-bar{background:var(--purple-dark);height:64px;color:#d6c9e6;font-size:11px;display:flex;align-items:center;justify-content:space-between;padding:0 60px}
</style>
</head>
<body>
<header class="site-header">
  <div class="brand"><span class="brand-mark"></span>K7 Electrical Services Ltd</div>
  <nav class="main-nav">
    <a class="active" href="#">Home</a><a href="#">About Us</a><a href="#">Our Services</a><a href="#">Latest Blog</a><a href="#">Contact Us</a>
  </nav>
</header>

<section class="hero">
  <div class="hero-photo" role="img" aria-label="Modern house with warm lit windows and garden at dusk"></div>
  <div class="hero-content">
    <h1 class="hero-title">K7 ELECTRICAL</h1>
    <p class="hero-tagline">We are a new electrical contracting company. We are customer service orientated</p>
  </div>
  <svg class="hero-wave" viewBox="0 0 1200 130" preserveAspectRatio="none"><path d="M0 40 Q600 180 1200 40 L1200 130 L0 130 Z" fill="#ffffff"/></svg>
</section>

<section class="welcome">
  <h2 class="section-heading">Welcome to K7 Electrical</h2>
  <p>Our team delivers safe, reliable electrical work for homes and businesses across the region. From first consultation to final inspection we plan every job carefully, use industry leading products and keep you informed at each step so projects finish on time and on budget.</p>
  <p>We specialise in custom residential and commercial upgrades, lighting design and energy efficient solutions. Whether you are a homebuilder, contractor or property manager, our certified electricians bring quality workmanship and friendly service to every site.</p>
</section>

<section class="about">
  <div class="about-photo" role="img" aria-label="City skyline at dusk with a purple tint"></div>
  <div class="about-content">
    <h2 class="section-heading">About K7 Electrical</h2>
    <p>Founded to raise the standard of electrical contracting, we combine modern design with proven installation methods. Our electricians hold full certification and take pride in clean, tidy work that lasts for years to come.</p>
    <a class="btn-outline" href="#">LEARN MORE</a>
  </div>
</section>

<section class="services">
  <h2 class="section-heading">Our Services</h2>
  <div class="service-list">
    <article class="service">
      <div class="service-icon"><svg width="80" height="80" viewBox="0 0 80 80" fill="none" stroke="#fff" stroke-width="5" stroke-linecap="round"><path d="M30 14v14M50 14v14"/><path d="M22 28h36v12a18 18 0 0 1-36 0z"/><path d="M40 58v12"/></svg></div>
      <h3>Electrical Installations</h3>
      <p>Complete wiring, panels and fittings for new builds and renovations to code.</p>
      <a class="btn-small" href="#">READ MORE ›</a>
    </article>
    <article class="service">
      <div class="service-icon"><svg width="80" height="80" viewBox="0 0 80 80" fill="none" stroke="#fff" stroke-width="5" stroke-linecap="round"><path d="M28 50a20 20 0 1 1 24 0v8H28z"/><path d="M30 66h20M34 73h12"/></svg></div>
      <h3>Electrical Design</h3>
      <p>Lighting layouts and power plans tailored to your space, style and energy goals.</p>
      <a class="btn-small" href="#">READ MORE ›</a>
    </article>
    <article class="service">
      <div class="service-icon"><svg width="80" height="80" viewBox="0 0 80 80" fill="none" stroke="#fff" stroke-width="5" stroke-linecap="round"><path d="M18 62l30-30"/><path d="M46 20a12 12 0 0 0 14 14l-6 6"/><path d="M20 18l42 44"/></svg></div>
      <h3>Electrical Maintenance</h3>
      <p>Scheduled checks, fault finding and repairs that keep your systems running.</p>
      <a class="btn-small" href="#">READ MORE ›</a>
    </article>
  </div>
</section>

<footer>
  <div class="site-footer">
    <div class="footer-about">
      <div class="brand"><span class="brand-mark"></span>K7 Electrical Services Ltd</div>
      <p>Licensed electrical contractors serving homes and businesses with quality installations, design and maintenance.</p>
    </div>
    <div class="footer-contact">
      <h4 class="footer-title">Contact Info</h4>
      <ul>
        <li><svg width="12" height="14" viewBox="0 0 12 14"><path d="M6 0a5 5 0 0 1 5 5c0 4-5 9-5 9S1 9 1 5a5 5 0 0 1 5-5z" fill="#fff"/></svg>K7 Electrical, 12 Harbour Street</li>
        <li><svg width="12" height="12" viewBox="0 0 12 12"><path d="M2 0h3l1 3-2 1a7 7 0 0 0 4 4l1-2 3 1v3a2 2 0 0 1-2 2A10 10 0 0 1 0 2a2 2 0 0 1 2-2z" fill="#fff"/></svg>+44 20 7946 0321</li>
        <li><svg width="13" height="10" viewBox="0 0 13 10"><rect width="13" height="10" fill="#fff"/><path d="M0 0l6.5 5L13 0" stroke="#5b2d8e" fill="none"/></svg>info@k7electrical.example</li>
      </ul>
    </div>
    <div class="footer-news">
      <h4 class="footer-title">Sign Up for Newsletters</h4>
      <p>Please sign up here for latest news</p>
      <div class="subscribe"><span></span><b>SUBSCRIBE</b></div>
      <div class="socials"><i></i><i></i><i></i><i></i></div>
    </div>
  </div>
  <div class="footer-bar"><span>© 2024 K7 Electrical. All rights reserved. Terms of Use</span><span>▲ Top</span></div>
</footer>
</body>
</html>
```